New Company Business Card Design

I have a new company logo and I want a new business card design. I dont know if the logo file i attached is in the correct format or quality. We are a New York City Specialty construction Firm specializing in high risk out of the box projects. I want a simple and classy business card that people will his card is as crisp as the work his company does.

Target Market(s)

Clients in the heavy construction industry in New York City

Industry/Entity Type

Construction Company

Contact Information for Business Card

Simple Classy - DIFFERENT

Font styles to use
Other font styles liked:
• Mach the logo font in some way

Colors

Designer to choose colors to be used in the design.

Requirements
Must have
• Uniqueness
Nice to have
• Nothing particular - Just different and classy - Timeless
Should not have
• Goofy Shit or Gimmicky shit

```html
<!DOCTYPE html>
<html lang="en">
<head>
<meta charset="utf-8">
<title>KRT Builders, Inc. — Business Card</title>
<link href="https://fonts.googleapis.com/css2?family=Roboto:wght@400;500;700&family=Montserrat:wght@500&display=swap" rel="stylesheet">
<style>
  :root {
    --backdrop: #333333;
    --card-front: #f1f1f1;
    --card-back: #151515;
    --brand-blue: #1f6bb0;
    --brand-blue-light: #2f8fd6;
    --text-dark: #4a4a4a;
    --rule: #9a9a9a;
    --text-light: #e6e6e6;
  }
  * { margin: 0; padding: 0; box-sizing: border-box; }
  html, body {
    width: 1200px; height: 986px; overflow: hidden;
    background: var(--backdrop);
    font-family: 'Roboto', sans-serif;
  }
  .stage { position: relative; width: 1200px; height: 986px; }
  .card {
    position: absolute; left: 341px; width: 518px; height: 296px;
  }
  .card--front { top: 160px; background: var(--card-front); }
  .card--back { top: 530px; background: var(--card-back); }

  .brand-name {
    position: absolute; left: 0; right: 0;
    text-align: center; font-weight: 700; letter-spacing: 1px;
    line-height: 1.05;
  }
  .card--front .brand-name { top: 40px; font-size: 40px; color: var(--brand-blue); }
  .card--back .brand-name { top: 96px; font-size: 52px; color: var(--brand-blue-light); }
  .brand-name small { display: block; font-size: 0.42em; letter-spacing: 5px; margin-top: 6px; }

  .person { position: absolute; top: 164px; left: 0; right: 0; text-align: center; }
  .person__name { font-size: 21px; font-weight: 500; color: var(--brand-blue); }
  .person__title { font-size: 14.5px; color: var(--text-dark); margin-top: 2px; }

  .address {
    position: absolute; top: 230px; left: 0; right: 0;
    text-align: center; font-size: 12px; color: var(--text-dark);
  }
  .rule {
    position: absolute; top: 252px; left: 61px; width: 397px;
    height: 1px; background: var(--rule);
  }
  .contacts {
    position: absolute; top: 259px; left: 0; right: 0;
    display: flex; justify-content: center; gap: 9px;
    font-size: 12px; color: var(--text-dark);
  }
  .contacts li { list-style: none; display: flex; align-items: center; gap: 5px; }
  .contacts svg { width: 11px; height: 11px; fill: var(--brand-blue); }

  .web {
    position: absolute; top: 254px; left: 0; right: 0; text-align: center;
    font-family: 'Montserrat', sans-serif; font-size: 12.5px;
    letter-spacing: 2.5px; color: var(--text-light);
  }
</style>
</head>
<body>
<main class="stage">
  <section class="card card--front">
    <div class="brand-name">KRT<small>BUILDERS, INC.</small></div>
    <div class="person">
      <div class="person__name">Marcus T. Ellery</div>
      <div class="person__title">President</div>
    </div>
    <p class="address">214 Harbor View Avenue, Bayonne, New Jersey 07002</p>
    <div class="rule"></div>
    <ul class="contacts">
      <li><svg viewBox="0 0 24 24"><path d="M6.6 10.8a15 15 0 0 0 6.6 6.6l2.2-2.2a1 1 0 0 1 1-.25 11.4 11.4 0 0 0 3.6.6 1 1 0 0 1 1 1V20a1 1 0 0 1-1 1A17 17 0 0 1 3 4a1 1 0 0 1 1-1h3.5a1 1 0 0 1 1 1c0 1.25.2 2.45.6 3.6a1 1 0 0 1-.25 1z"/></svg>908-555-0142</li>
      <li><svg viewBox="0 0 24 24"><path d="M7 1h10a2 2 0 0 1 2 2v18a2 2 0 0 1-2 2H7a2 2 0 0 1-2-2V3a2 2 0 0 1 2-2zm0 3v14h10V4zm5 15.5a1 1 0 1 0 0 2 1 1 0 0 0 0-2z"/></svg>917-555-0187</li>
      <li><svg viewBox="0 0 24 24"><path d="M2 5h20v14H2zm2 2v.5l8 5 8-5V7z"/></svg>MARCUS@KRTBUILD.COM</li>
      <li><svg viewBox="0 0 24 24"><path d="M12 2a10 10 0 1 0 0 20 10 10 0 0 0 0-20zm7.9 9h-3.9a15 15 0 0 0-1.4-6.4A8 8 0 0 1 19.9 11zM12 4.1c.9 1.2 1.8 3.5 2 6.9h-4c.2-3.4 1.1-5.7 2-6.9zM9.4 4.6A15 15 0 0 0 8 11H4.1a8 8 0 0 1 5.3-6.4zM4.1 13H8a15 15 0 0 0 1.4 6.4A8 8 0 0 1 4.1 13zm7.9 6.9c-.9-1.2-1.8-3.5-2-6.9h4c-.2 3.4-1.1 5.7-2 6.9zm2.6-.5A15 15 0 0 0 16 13h3.9a8 8 0 0 1-5.3 6.4z"/></svg>KRTBUILD.COM</li>
    </ul>
  </section>

  <section class="card card--back">
    <div class="brand-name">KRT<small>BUILDERS, INC.</small></div>
    <p class="web">KRTBUILD.COM</p>
  </section>
</main>
</body>
</html>
```